Stainless steel BBQ set Package

We need a package/box design for a barbecue set. It is a 20 piece set with a 2nd cleaning brush attachment free. The set is high quality stainless steel and comes with its own travel/storage case.

I'm going to attach the old package that the company in China sent me with the dimensions in CentiMeter not Inches but we can always convert.

FEEL FREE TO BE ENTIRELY CREATIVE, USING PART/ALL OF REAL PRODUCT PHOTO.
IF THE REAL PRODUCT PHOTOS DO NOT LOOK PROFESSIONAL, DO NOT INCLUDE.
Updates

Industry/Entity Type

Steel

Requirements
Must have
• *Name: Ember Forge
*Brought to you by BrixoMart (include logo)
*Mention that is 20 pieces, high grade, stainless steel barbecue/grilling tool set, which includes the following:
1-Knife, 1-Fork, 1-Spatula, 1-Tongs, 8-Skewers & 8-Corn Holders, 1-Cleaning Brush w/ 1 additional head-FREE).
*Also, in small/fine print, please include Made in China and near and/or on the same side as barcode
Barcode should be on the side (not front/back)

Barcode Requirements:
The nominal size for a UPC Barcode is 1.5 inches wide by 1 inch high, but you may adjust it to fit your packaging up to twice the nominal size and down to 80% of the nominal size and still meet UPC Standards. You may have to adjust the size using your image processing software after you save it for use on your package
Should not have
• If pictures do not look good on packaging, please do not include. Yet, be creative to bring more appeal to what's inside.

```html
<!DOCTYPE html>
<html lang="en">
<head>
<meta charset="utf-8">
<title>Ember Forge – 20 Piece Stainless Steel BBQ Tool Set</title>
<link rel="stylesheet" href="https://fonts.googleapis.com/css2?family=Josefin+Sans:ital,wght@0,400;0,600;0,700;1,700&display=swap">
<style>
  :root {
    --page-light: #f4f4f4;
    --page-dark: #d9d9d9;
    --panel-top: #262626;
    --panel-mid: #0b0b0b;
    --panel-bottom: #161616;
    --ink: #ffffff;
    --ink-soft: #e6e6e6;
    --ink-fine: #9a9a9a;
    --steel-light: #f2f2f2;
    --steel-dark: #9a9a9a;
  }
  html, body {
    margin: 0;
    width: 1200px;
    height: 857px;
    overflow: hidden;
  }
  body {
    background: radial-gradient(ellipse at 50% 40%, var(--page-light) 0%, var(--page-dark) 100%);
    font-family: "Josefin Sans", "Futura", sans-serif;
    color: var(--ink);
    position: relative;
  }
  .package-panel {
    position: absolute;
    left: 50px;
    top: 163px;
    width: 1100px;
    height: 529px;
    border-radius: 22px;
    background: linear-gradient(180deg, var(--panel-top) 0%, var(--panel-mid) 45%, var(--panel-mid) 75%, var(--panel-bottom) 100%);
    box-shadow: 0 6px 14px rgba(0,0,0,0.35);
  }
  .product-title {
    position: absolute;
    left: 55px;
    top: 34px;
    margin: 0;
    font-size: 28px;
    font-weight: 400;
    letter-spacing: 2.4px;
    white-space: nowrap;
  }
  .product-title strong {
    font-weight: 700;
    font-style: italic;
  }
  .retailer-mark {
    position: absolute;
    left: 836px;
    top: 32px;
    display: flex;
    align-items: center;
    gap: 10px;
    font-size: 34px;
    font-weight: 600;
    letter-spacing: -0.5px;
  }
  .retailer-mark .mark-dot {
    width: 16px;
    height: 16px;
    background: var(--ink);
    border-radius: 50%;
  }
  .spec-block {
    position: absolute;
    left: 87px;
  }
  .spec-block h2 {
    margin: 0 0 4px;
    font-size: 26px;
    font-weight: 400;
    letter-spacing: 1.6px;
  }
  .spec-block ul {
    margin: 0;
    padding: 0;
    list-style: none;
  }
  .spec-block li {
    font-size: 20px;
    line-height: 28px;
    letter-spacing: 1.3px;
    color: var(--ink-soft);
    white-space: nowrap;
  }
  .spec-block li::before {
    content: "•";
    margin-right: 1px;
  }
  .features { top: 125px; }
  .contents { top: 300px; }
  .brand-emblem {
    position: absolute;
    left: 640px;
    top: 112px;
    width: 420px;
    text-align: center;
  }
  .brand-name {
    margin: 0;
    font-size: 50px;
    font-weight: 700;
    line-height: 56px;
  }
  .brand-circle {
    display: block;
    margin: 8px auto 8px;
  }
  .brand-slogan {
    margin: 0;
    font-size: 24px;
    font-weight: 600;
  }
  .fine-print {
    position: absolute;
    right: 28px;
    bottom: 16px;
    margin: 0;
    font-size: 11px;
    letter-spacing: 1px;
    color: var(--ink-fine);
  }
</style>
</head>
<body>
  <main class="package-panel">
    <h1 class="product-title">20 PIECE STAINLESS STEEL <strong>BBQ TOOL SET</strong></h1>

    <div class="retailer-mark"><span class="mark-dot"></span>BrixoMart</div>

    <section class="spec-block features">
      <h2>PRODUCT FEATURES:</h2>
      <ul>
        <li>High grade stainless steel tools</li>
        <li>Heavy duty aluminum carrying case</li>
        <li>Stainless steel trim/carrying handle</li>
        <li>Fabric inner liner throughout</li>
      </ul>
    </section>

    <section class="spec-block contents">
      <h2>SET INCLUDES</h2>
      <ul>
        <li>1 Knife &amp; 1 Fork</li>
        <li>1 Spatula</li>
        <li>1 Tongs</li>
        <li>8 Skewers &amp; 8 Corn holders</li>
        <li>1 Cleaning brush</li>
        <li>1 Extra brush head – FREE</li>
      </ul>
    </section>

    <div class="brand-emblem">
      <p class="brand-name">Ember Forge</p>
      <svg class="brand-circle" width="236" height="236" viewBox="0 0 200 200" role="img" aria-label="Brand emblem: steel grill grate">
        <defs>
          <radialGradient id="steelFill" cx="40%" cy="35%" r="75%">
            <stop offset="0%" stop-color="var(--steel-light)"/>
            <stop offset="100%" stop-color="var(--steel-dark)"/>
          </radialGradient>
        </defs>
        <circle cx="100" cy="100" r="96" fill="url(#steelFill)"/>
      </svg>
      <p class="brand-slogan">your slogan goes here</p>
    </div>

    <p class="fine-print">Made in China</p>
  </main>
</body>
</html>
```